Bramblewood Counselling Group Pty Ltd

clinical psychologist in private practice needs professional stationery package: business cards, complimentary slips, envelopes, range of business letterheads, and logo (photo of lighthouse).

I work with children, adolescents, adults and older population with a range of mental health concerns, adjustment to life transitions and learning difficulties. Majority of my correspondence is with medical practitioners writing reports. I would a clean crisp professional presentation (white background, navy blue text but open to ideas). Thought about having lighthouse as watermark on envelopes. My professional organisation (GTC) logo needs to be on business cards and templates (manual gives guidelines),. The photo of lighthouse is to be included in logo.
There needs to be three letterheads. 1.Is Company only Detail "bramblewood Counselling Group Pty Ltd". 2. Include Company detail and Moira Fensham Clinical Psychologist information at KVRT. 3. Include Company detail and Moira Fensham Clinical Psychologist information at Orchardvale Medical Centre

Target Market(s)

Doctors

Industry/Entity Type

Business

Colors
0355a3
3176b5
0592cd
33a6d7

Requirements
Must have
• Picture of the lighthouse
• GTC logo
• Business name

```html
<!DOCTYPE html>
<html lang="en">
<head>
<meta charset="utf-8">
<title>Bramblewood Counselling Group – Stationery</title>
<link href="https://fonts.googleapis.com/css2?family=PT+Sans+Narrow:wght@400;700&family=Carlito:wght@400;700&family=Alegreya:wght@500&display=swap" rel="stylesheet">
<style>
:root{
  --navy:#0355a3;
  --mid-blue:#3176b5;
  --bright-blue:#0592cd;
  --sky:#33a6d7;
  --ink:#222;
  --grey-text:#555;
  --backdrop:#a3a3a3;
  --paper:#fff;
  --mark-light:#eef1f3;
  --mark-dark:#d3d8dd;
  --flap:#0d57a6;
  --flap-light:#5d8fca;
}
*{margin:0;padding:0;box-sizing:border-box}
html,body{width:1200px;height:1000px;overflow:hidden}
body{background:radial-gradient(circle at 50% 45%,#b0b0b0,var(--backdrop) 70%);position:relative;font-family:"Carlito",sans-serif;color:var(--ink)}
.sheet{position:absolute;background:var(--paper);box-shadow:9px 9px 12px rgba(0,0,0,.45)}
.abs{position:absolute}

/* brand lock-up */
.brand-mark{position:absolute;background:linear-gradient(90deg,#8b97a3,#d8dde2 50%,#7e8a96)}
.brand-name{position:absolute;font-family:"PT Sans Narrow",sans-serif;font-weight:700;color:var(--navy);line-height:1;white-space:nowrap}
.brand-name span{display:block}

/* faint photo watermark area */
.photo-watermark{position:absolute;background:linear-gradient(180deg,rgba(255,255,255,0),var(--mark-light) 18%,var(--mark-dark));}

/* contact lines */
.contact{font-family:"PT Sans Narrow",sans-serif;color:var(--ink);white-space:nowrap;display:flex;align-items:center}
.contact svg{flex:none;fill:var(--navy)}
.address{font-family:"PT Sans Narrow",sans-serif;font-weight:700;color:var(--mid-blue);white-space:nowrap;line-height:1.35}

/* membership badge */
.badge{position:absolute;display:flex;align-items:center;z-index:2}
.badge-seal{border-radius:50%;background:#222;flex:none}
.badge-text{font-family:"PT Sans Narrow",sans-serif;color:#222;line-height:1.05;border-left:1px solid #333;white-space:nowrap}

/* business card */
.card{left:47px;top:43px;width:333px;height:207px}
.card .rule{left:143px;top:78px;width:190px;height:1px;background:var(--sky)}
.card .person{right:23px;top:36px;font-family:"PT Sans Narrow",sans-serif;font-weight:700;font-size:16px;color:var(--navy)}
.card .quals{right:26px;top:58px;text-align:right;font-family:"PT Sans Narrow",sans-serif;font-size:8.5px;color:var(--grey-text);line-height:1.25}
.card .contact{font-size:11.5px;gap:5px}

/* letterhead */
.letterhead{left:47px;top:287px;width:481px;height:680px;overflow:hidden}
.letterhead .info{left:375px;top:26px;border-left:1px solid var(--sky);padding-left:6px;height:60px}
.letterhead .info .contact{font-size:7.5px;gap:3px;height:10px}
.letterhead .abn{font-family:"PT Sans Narrow",sans-serif;font-weight:700;font-size:7.5px;color:var(--navy);margin-top:4px}
.letter-body{left:40px;top:134px;width:392px;font-size:9.5px;line-height:17.2px;color:#222;z-index:1}
.letter-body p{margin-bottom:17px}
.signature{left:34px;top:507px;width:122px;height:44px;background:linear-gradient(90deg,rgba(0,0,0,.05),rgba(0,0,0,.15),rgba(0,0,0,.05));border-radius:20px}

/* compliments slip */
.slip{left:586px;top:178px;width:490px;height:216px;overflow:hidden}
.slip .heading{right:18px;top:11px;font-family:"Alegreya",serif;font-weight:500;font-size:15px;color:var(--navy)}
.slip .col{top:183px;border-left:1px solid var(--sky);padding-left:5px}
.slip .contact{font-size:6px;gap:2px;height:9px}
.slip .address{font-size:6.5px;line-height:9px}

/* envelope front */
.env-front{left:586px;top:456px;width:550px;height:242px;overflow:hidden}
.env-front .contact{font-size:6.5px;gap:3px;height:9px}
.env-front .address{font-size:6.5px;line-height:9px}

/* envelope back */
.env-back{left:586px;top:723px;width:550px;height:244px;overflow:hidden}
</style>
</head>
<body>

<!-- Business card -->
<section class="sheet card">
  <div class="brand-mark" role="img" aria-label="Lighthouse photograph logo" style="left:26px;top:28px;width:9px;height:54px"></div>
  <div class="brand-name" style="left:51px;top:59px;font-size:14px"><span>BRAMBLEWOOD</span><span style="font-size:8.5px;margin-top:2px">Counselling Group PTY LTD</span></div>
  <div class="abs rule"></div>
  <div class="abs person">Moira Fensham</div>
  <div class="abs quals">BSc(Psych); BSc(Hons); GradDipEd<br>MPsych(Clinical); MGTC</div>
  <div class="abs" style="left:25px;top:97px">
    <div class="contact"><svg width="9" height="9" viewBox="0 0 10 10"><path d="M1 3c0-2 8-2 8 0v1H7V3H3v1H1zM2 5h6l1 4H1z"/></svg>07 4519 2736</div>
    <div class="contact" style="margin-top:1px"><svg width="9" height="9" viewBox="0 0 10 10"><path d="M1 2h2v7H1zM4 4h5v5H4zM5 1h3v2H5z"/></svg>07 4519 2736</div>
    <div class="contact" style="margin-top:9px"><svg width="9" height="9" viewBox="0 0 10 10"><path d="M1 2h8v6H1z M1 2l4 3 4-3" stroke="#fff" stroke-width=".6"/></svg>admin@kvrt.com.au</div>
    <div class="contact" style="margin-top:1px"><svg width="9" height="9" viewBox="0 0 10 10"><circle cx="5" cy="5" r="4"/><path d="M1 5h8M5 1v8" stroke="#fff" stroke-width=".6"/></svg>www.kvrt.com.au</div>
    <div class="address" style="font-size:11px;margin-top:1px">Suite 3, 12 Harlow St.<br>Eastmere, Q 4371</div>
  </div>
  <div class="badge" style="left:213px;top:156px">
    <div class="badge-seal" role="img" aria-label="Professional body membership badge" style="width:22px;height:22px;margin-right:6px"></div>
    <div class="badge-text" style="font-size:7px;padding-left:5px">Member<br>Guild of<br>Therapeutic<br>Counsellors MGTC</div>
  </div>
</section>

<!-- Letterhead -->
<section class="sheet letterhead">
  <div class="brand-mark" role="img" aria-label="Lighthouse photograph logo" style="left:45px;top:23px;width:12px;height:65px"></div>
  <div class="brand-name" style="left:70px;top:60px;font-size:16px"><span>BRAMBLEWOOD</span><span style="font-size:10px;margin-top:3px">Counselling Group PTY LTD</span></div>
  <div class="abs info">
    <div class="contact"><svg width="7" height="7" viewBox="0 0 10 10"><path d="M1 3c0-2 8-2 8 0v1H7V3H3v1H1zM2 5h6l1 4H1z"/></svg>07 4519 2736</div>
    <div class="contact"><svg width="7" height="7" viewBox="0 0 10 10"><path d="M1 2h2v7H1zM4 4h5v5H4zM5 1h3v2H5z"/></svg>07 4519 2736</div>
    <div class="contact" style="margin-top:3px"><svg width="7" height="7" viewBox="0 0 10 10"><path d="M1 2h8v6H1z"/></svg>admin@kvrt.com.au</div>
    <div class="contact"><svg width="7" height="7" viewBox="0 0 10 10"><circle cx="5" cy="5" r="4"/></svg>www.kvrt.com.au</div>
    <div class="abn">ABN: 48 302 775 104</div>
  </div>
  <div class="photo-watermark" role="img" aria-label="Faint lighthouse photograph watermark" style="left:383px;top:355px;width:95px;height:325px"></div>
  <div class="abs letter-body">
    <p style="margin-bottom:0">To<br>Mr. Peter Caldwell<br>Lorem Ipsum is simply a dummy text</p>
    <p style="margin-top:17px">&nbsp;dummy text of the printing and typesetting industry. Lorem Ipsum has been the industry's standard dummy text ever since the 1500s, when an unknown printer took a galley of type and scrambled it to make a type specimen book. It has survived not only five centuries, but also the leap into electronic typesetting, remaining essentially unchanged. It was popularised in the 1960s with the release</p>
    <p>It is a long established fact that a reader will be distracted by the readable content of a page when lookidesktop publishing packages and web page editors now use Lorem Ipsum as their default model text, and a search for 'lorem ipsum' will uncover many web sites still in their infancy. Various versions have evolved over the years, sometimes by accident, sometimes on purpose (injected humour and the like).</p>
    <p>&nbsp;a Latin professor at Wexbridge College in Norfolk, looked up one of the more obscure Latin words, consectetur, from a Lorem Ipsum passage, and going through the cites of the word in classical literature, discovered the undoubtable source. Lorem Ipsum comes from sections 1.10.32 and 1.10.33 of "de Finibus Bonorum et Malorum" (The Extremes of Good and Evil) by Aurelian, written in 45 BC. This book</p>
    <p>Lorem Ipsum</p>
  </div>
  <div class="abs signature" role="img" aria-label="Handwritten signature"></div>
  <div class="abs" style="left:40px;top:560px;font-size:9.5px">Lorem Ipsum is a dummy</div>
  <div class="badge" style="left:346px;top:628px">
    <div class="badge-seal" role="img" aria-label="Professional body membership badge" style="width:22px;height:22px;margin-right:6px"></div>
    <div class="badge-text" style="font-size:7px;padding-left:5px">Member<br>Guild of<br>Therapeutic<br>Counsellors MGTC</div>
  </div>
</section>

<!-- Compliments slip -->
<section class="sheet slip">
  <div class="abs heading">With Compliments</div>
  <div class="photo-watermark" role="img" aria-label="Faint lighthouse photograph watermark" style="left:430px;top:47px;width:62px;height:169px"></div>
  <div class="brand-mark" role="img" aria-label="Lighthouse photograph logo" style="left:20px;top:164px;width:7px;height:40px"></div>
  <div class="brand-name" style="left:36px;top:187px;font-size:10px"><span>BRAMBLEWOOD</span><span style="font-size:5.5px;margin-top:2px">Counselling Group PTY LTD</span></div>
  <div class="abs col" style="left:112px">
    <div class="contact"><svg width="6" height="6" viewBox="0 0 10 10"><path d="M1 3c0-2 8-2 8 0v1H7V3H3v1H1zM2 5h6l1 4H1z"/></svg>07 4519 2736</div>
    <div class="contact"><svg width="6" height="6" viewBox="0 0 10 10"><path d="M1 2h2v7H1zM4 4h5v5H4z"/></svg>07 4519 2736</div>
  </div>
  <div class="abs col" style="left:168px">
    <div class="contact"><svg width="6" height="6" viewBox="0 0 10 10"><path d="M1 2h8v6H1z"/></svg>admin@kvrt.com.au</div>
    <div class="contact"><svg width="6" height="6" viewBox="0 0 10 10"><circle cx="5" cy="5" r="4"/></svg>www.kvrt.com.au</div>
  </div>
  <div class="abs col" style="left:240px">
    <div class="address">Suite 3, 12 Harlow St.<br>Eastmere, Q 4371</div>
  </div>
  <div class="badge" style="left:405px;top:179px">
    <div class="badge-seal" role="img" aria-label="Professional body membership badge" style="width:14px;height:14px;margin-right:4px"></div>
    <div class="badge-text" style="font-size:5px;padding-left:3px">Member<br>Guild of<br>Therapeutic<br>Counsellors</div>
  </div>
</section>

<!-- Envelope front -->
<section class="sheet env-front">
  <div class="brand-mark" role="img" aria-label="Lighthouse photograph logo" style="left:20px;top:14px;width:6px;height:30px"></div>
  <div class="brand-name" style="left:32px;top:31px;font-size:9px"><span>BRAMBLEWOOD</span><span style="font-size:5px;margin-top:1px">Counselling Group PTY LTD</span></div>
  <div class="abs" style="left:17px;top:51px">
    <div class="contact"><svg width="6" height="6" viewBox="0 0 10 10"><path d="M1 2h8v6H1z"/></svg>admin@kvrt.com.au</div>
    <div class="contact"><svg width="6" height="6" viewBox="0 0 10 10"><circle cx="5" cy="5" r="4"/></svg>www.kvrt.com.au</div>
    <div class="address" style="margin-top:1px">Suite 3, 12 Harlow St.<br>Eastmere, Q 4371</div>
  </div>
  <div class="photo-watermark" role="img" aria-label="Faint lighthouse photograph watermark" style="left:480px;top:58px;width:70px;height:184px"></div>
</section>

<!-- Envelope back -->
<section class="sheet env-back">
  <svg class="abs" style="left:0;top:0" width="550" height="70" viewBox="0 0 550 70" role="img" aria-label="Envelope flap">
    <path d="M0 0H550L530 40Q522 64 500 64H50Q28 64 20 40Z" fill="var(--flap)"/>
  </svg>
  <div class="abs" role="img" aria-label="Small lighthouse photograph mark" style="left:267px;top:10px;width:14px;height:43px;background:var(--flap-light)"></div>
</section>

</body>
</html>
```